Private Investment Firm Needs PowerPoint Presentation Template

Design PowerPoint template, take Ridgefell-submitted rough presentation draft, and drop it into new template. See attached Project Brief file for more detail.
Updates

Some decent designs have been submitted but they seem to lack the understanding of our target markets. I am hopeful that more time and feedback will result in better results.

Target Market(s)

Private company owners and intermediaries.

Font styles to use
Serif

Colors
3176b5

Requirements
Must have
• See attached Project Brief.
Nice to have
Should not have
• No B2C fluff--this is a B2B project.

```html
<!DOCTYPE html>
<html lang="en">
<head>
<meta charset="utf-8">
<title>Ridgefell – Introduction to Non-Control Capital</title>
<link href="https://fonts.googleapis.com/css2?family=Libre+Baskerville:wght@400;700&family=Source+Sans+3:wght@400;600;700&family=Arimo:wght@400;700&display=swap" rel="stylesheet">
<style>
  :root{
    --brand:#3176b5;
    --brand-dark:#1f4e79;
    --ink:#222;
    --panel:#f2f2f2;
    --band:#4a88c9;
    --teal:#1c8a6e;
    --dot:#c9c9c9;
  }
  *{box-sizing:border-box;margin:0;padding:0}
  html,body{width:1200px;height:1010px;overflow:hidden;background:#fff}
  body{position:relative;font-family:"Source Sans 3",Calibri,sans-serif;color:var(--ink)}
  .slide{position:absolute;overflow:hidden;background:#fff}
  .abs{position:absolute}
  .serif{font-family:"Libre Baskerville",Georgia,serif}
  .sans{font-family:"Source Sans 3",Calibri,sans-serif}

  /* footer name tag */
  .name-tag{position:absolute;display:flex;align-items:center;gap:5px}
  .name-tag .dot{width:11px;height:11px;border-radius:50%;background:var(--brand)}
  .name-tag .name{font-family:"Source Sans 3",Calibri,sans-serif;font-weight:600;color:var(--brand-dark);font-size:12px}
  .page-no{position:absolute;width:24px;height:24px;border-radius:50%;background:var(--teal);color:#fff;font-size:8px;display:flex;align-items:center;justify-content:center}

  /* slide 1 */
  .s1{left:0;top:0;width:596px;height:336px}
  .s1 .title-name{left:0;width:716px;top:112px;display:flex;justify-content:center;align-items:center;gap:12px}
  .s1 .title-name .dot{width:34px;height:34px;border-radius:50%;background:var(--brand)}
  .s1 .title-name .name{font-family:"Source Sans 3",Calibri,sans-serif;font-weight:600;font-size:34px;color:var(--brand-dark)}
  .s1 .deck-title{left:0;width:716px;top:188px;text-align:center;font-size:17px;color:var(--brand);letter-spacing:.5px}
  .s1 .deck-sub{left:0;width:716px;top:210px;text-align:center;font-family:"Arimo",Arial,sans-serif;font-size:11.5px;line-height:14px}
  .s1 .season{left:440px;top:303px;font-size:11px;font-weight:700}

  /* slide 2 */
  .s2{left:598px;top:0;width:602px;height:336px}
  .s2 .band{left:506px;top:0;width:80px;height:336px;background:var(--band)}
  .s2 .photo{left:370px;top:64px;width:194px;height:209px;background:linear-gradient(135deg,#e9eef3,#b9c6d3 55%,#5c6f86)}
  .s2 h2{left:34px;top:36px;font-size:19px;color:var(--brand-dark);font-weight:700}
  .s2 .body{left:34px;top:72px;width:332px;font-size:10.4px;line-height:12.3px}
  .s2 .body p{margin-bottom:12px}
  .s2 .body ul{list-style:none;margin-bottom:12px}
  .s2 .body li{padding-left:16px;position:relative}
  .s2 .body li:before{content:"•";position:absolute;left:0}

  /* slide 3 */
  .s3{left:0;top:336px;width:596px;height:336px}
  .heading{position:absolute;left:0;width:100%;text-align:center;font-family:"Source Sans 3",Calibri,sans-serif;font-weight:700;color:var(--brand-dark)}
  .dots{position:absolute;display:flex;gap:4px}
  .dots i{width:7px;height:7px;border-radius:50%;background:var(--dot)}
  .dots.blue i{background:var(--brand)}
  .s3 .box{position:absolute;left:50px;width:492px;background:var(--panel);border-radius:10px;font-size:10.4px;line-height:12.5px}
  .s3 .num{position:absolute;width:32px;height:32px;border-radius:50%;background:var(--brand);color:#fff;border:2px solid #1f4e79;font-size:14px;display:flex;align-items:center;justify-content:center}
  .s3 ul{list-style:none}
  .s3 li{position:relative;padding-left:12px}
  .s3 li:before{content:"•";position:absolute;left:0}

  /* slide 4 */
  .s4{left:598px;top:336px;width:602px;height:336px}
  .s4 .band{left:0;top:170px;width:602px;height:166px;background:var(--band)}
  .s4 .panel{left:45px;top:38px;width:509px;height:268px;background:var(--panel)}
  .s4 ul{position:absolute;left:60px;top:93px;list-style:none;font-size:13px;line-height:19.8px}
  .s4 li{position:relative;padding-left:12px}
  .s4 li:before{content:"•";position:absolute;left:0}
  .s4 li.sub{padding-left:34px;font-size:12px}
  .s4 li.sub:before{left:22px}

  /* slide 5 */
  .s5{left:0;top:672px;width:604px;height:338px}
  .s5 .photo{left:0;top:0;width:604px;height:338px;background:linear-gradient(120deg,#6d6a66,#c8b9a4 45%,#e9e2d6 70%,#8b8580)}
  .s5 .quote{left:46px;top:38px;width:228px;height:228px;border-radius:50%;background:#fff;text-align:center;padding:30px 24px 0;font-size:11px;line-height:13.6px}
  .s5 .quote .mark{font-size:18px;color:var(--brand-dark);line-height:10px}
  .s5 .quote .by{color:var(--brand);margin-top:12px}

  /* slide 6 */
  .s6{left:604px;top:672px;width:596px;height:338px}
  .s6 .row{position:absolute;left:0;width:596px;display:grid;grid-template-columns:repeat(4,1fr);align-items:center;text-align:center}
  .s6 .row.r1{top:54px;height:86px;background:var(--band);color:#fff}
  .s6 .row.r2{top:140px;height:88px;background:var(--panel)}
  .s6 .row.r3{top:228px;height:90px}
  .s6 h4{font-size:11.5px;line-height:13px;font-weight:700;margin-bottom:2px}
  .s6 p{font-family:"Arimo",Arial,sans-serif;font-size:6.4px;line-height:8px;padding:0 6px}
  .s6 .r1 h4{color:#fff}
  .s6 .r1 p{color:#e3eefa}
</style>
</head>
<body>

<section class="slide s1">
  <div class="abs title-name"><span class="dot"></span><span class="name">Ridgefell</span></div>
  <div class="abs deck-title serif">INTRODUCTION TO NON-CONTROL CAPITAL</div>
  <div class="abs deck-sub">The Lower Middle Market Private Company Strategy for Raising Capital<br>While Maintaining Business Control</div>
  <div class="abs season serif">Fall 2018</div>
</section>

<section class="slide s2">
  <div class="abs band"></div>
  <div class="abs photo" role="img" aria-label="Photo of three colleagues reviewing a document together"></div>
  <h2 class="abs">INTRODUCTION</h2>
  <div class="abs body">
    <p style="margin-bottom:2px">Private company owners have traditionally considered two capital raising options:</p>
    <ul>
      <li>Borrow from a local bank, or</li>
      <li>Sell most or all of the company to a change-of-control investor (aka Buyout firm)</li>
    </ul>
    <p>An alternative most have not considered is the raising of Non-Control Capital, or capital that is invested into the business yet allows those same owners to retain controlling interest in their company</p>
    <p>Non-Control Capital is not appropriate for every private company owner but neither is a Change-of-Control sale</p>
    <p>The key is to determine what the business and owners require, and then partner with an investor best aligned with those needs so that long-term company growth, and personal goals, can both be achieved</p>
  </div>
  <div class="name-tag" style="left:4px;top:310px"><span class="dot"></span><span class="name">Ridgefell</span></div>
  <div class="page-no" style="left:552px;top:310px">2</div>
</section>

<section class="slide s3">
  <div class="heading" style="top:10px;font-size:26px">What is Non-Control Capital?</div>
  <div class="dots" style="left:276px;top:44px"><i></i><i></i><i></i></div>

  <div class="box" style="top:76px;height:104px;padding:10px 14px 0 22px">
    <ul>
      <li>Non-Control Capital is an investment which is primarily used for the ongoing operation and/or growth of a business but <b><u>also</u></b> allows the current owners to retain:</li>
    </ul>
    <ul style="margin-top:10px;line-height:14px">
      <li>Control of the business economics</li>
      <li>Control of the business operations</li>
      <li>Control of strategy and key decision making</li>
      <li>Control of the Board of Directors</li>
    </ul>
  </div>
  <div class="num" style="left:29px;top:96px">1</div>

  <div class="box" style="top:198px;height:28px;padding:7px 0 0 26px">Requires the alignment of management incentives with ownership</div>
  <div class="num" style="left:32px;top:197px">2</div>

  <div class="box" style="top:246px;height:35px;padding:5px 4px 0 22px;text-align:center">In essence, a company receives the capital it needs to implement its business plans but owners continue to retain ultimate control</div>
  <div class="num" style="left:32px;top:246px">3</div>

  <div class="name-tag" style="left:4px;top:308px"><span class="dot"></span><span class="name">Ridgefell</span></div>
  <div class="page-no" style="left:562px;top:306px">3</div>
</section>

<section class="slide s4">
  <div class="abs band"></div>
  <div class="abs panel"></div>
  <div class="heading" style="top:40px;font-size:21px">When is a Non-Control Transaction Appropriate?</div>
  <div class="dots blue" style="left:290px;top:72px"><i></i><i></i><i></i></div>
  <ul>
    <li>The company has opportunities to expand but requires capital to do so</li>
    <li>At least one active owner <b><u>is not</u></b> close to retirement</li>
    <li>The company is not in a turnaround situation</li>
    <li>Family members may work in the business and want to continue</li>
    <li>Owners care about keeping the business in their family name (legacy)</li>
    <li>Liquidity (dividend) is not the major use of the invested capital</li>
    <li>Owners are sensitive to utilizing too much debt</li>
    <li>Companies require more than just capital:</li>
    <li class="sub">They may also need operational, marketing, financial, and/or technology counsel</li>
  </ul>
  <div class="name-tag" style="left:6px;top:310px"><span class="dot"></span><span class="name" style="color:#fff">Ridgefell</span></div>
  <div class="page-no" style="left:563px;top:308px">4</div>
</section>

<section class="slide s5">
  <div class="abs photo" role="img" aria-label="Photo of a business handshake over a desk with a laptop"></div>
  <svg class="abs" style="left:20px;top:12px" width="280" height="280" viewBox="0 0 280 280" aria-hidden="true">
    <circle cx="140" cy="140" r="134" fill="none" stroke="#fff" stroke-width="1"/>
    <circle cx="140" cy="140" r="127" fill="none" stroke="#fff" stroke-width="1"/>
  </svg>
  <div class="abs quote">
    <div class="mark">&ldquo;</div>
    Our company<br>had several business opportunities but I needed outside capital to take advantage of them. Why would I cede control of my business when we were at the exact point when raising outside capital would allow me to accelerate growth and achieve my life-long business and personal goals?!
    <div class="by">Daniel Hartley, CEO<br>The Norland Group</div>
  </div>
  <div class="name-tag" style="left:8px;top:308px"><span class="dot"></span><span class="name">Ridgefell</span></div>
  <div class="page-no" style="left:569px;top:310px">5</div>
</section>

<section class="slide s6">
  <div class="heading" style="top:8px;font-size:24px">The 12 Primary Uses of Non-Control Capital</div>
  <div class="dots" style="left:281px;top:39px"><i></i><i></i><i></i></div>

  <div class="row r1">
    <div><h4>Growth</h4><p>Capital used to organically expand a business: introduce new products, build a new factory, hire additional management or employees, enter new markets, or for general working capital purposes</p></div>
    <div><h4>Acquisitions</h4><p>Capital used to acquire one or more competitors or to allow for further vertical or horizontal integration</p></div>
    <div><h4>Partner or Shareholder Buy-Out</h4><p>Capital used to buy-out an inactive or retiring partner or shareholder</p></div>
    <div><h4>Management Buy-Out (MBO)</h4><p>When the incumbent management team buys most or all of the ownership of an inactive founder or executive</p></div>
  </div>
  <div class="row r2">
    <div><h4>Management Buy-In (MBI)</h4><p>When an external, experienced executive buys a business from one or more inactive owners and needs additional capital to affect the purchase</p></div>
    <div><h4>Family Ownership &amp; Wealth Transfer</h4><p>When junior generations of a family acquire most or all of the ownership interests of more senior generations allowing the business to remain in the family name</p></div>
    <div><h4>Balance Sheet Recapitalization</h4><p>Changes the debt and equity mixture of a Company's finances to a more optimal capital structure</p></div>
    <div><h4>Refinancing</h4><p>Replacing one form or type of debt with another with better terms, conditions, and flexibility</p></div>
  </div>
  <div class="row r3">
    <div><h4>Family Office Support</h4><p>Allows a Family Office to affect an investment in a Company by allowing a junior capital provider to invest alongside them</p></div>
    <div><h4>Senior Lender Enhancement or Transition</h4><p>When a Company has grown beyond the means or interest of its senior bank but needs additional capital to support its continuing growth</p></div>
    <div><h4>De-Lever Balance Sheet</h4><p>When a Company has taken on too much debt (typically senior debt) and replaces some of it with either equity or other junior capital to provide operating flexibility</p></div>
    <div><h4>Owner Dividend (Liquidity)</h4><p>When one or more owners take a non-life changing cash distribution, typically used to diversify their net worth</p></div>
  </div>

  <div class="name-tag" style="left:10px;top:312px"><span class="dot"></span><span class="name">Ridgefell</span></div>
  <div class="page-no" style="left:566px;top:310px">6</div>
</section>

</body>
</html>
```